Wren's Home Care Retractable Banner Design

Retractable Banner Design
We need a pull up retractable banner design
85 x 206 cm.
We need the banner to use at expo's, information sessions, presentations, recruitment days. Needs to be attractive to our elderly client's and staff (care workers)
Phone number needs to be on 08 7394 2650
Website also needs to be on the banner : wrenshomecare-example.com.au

Target Market(s)

35 +

Industry/Entity Type

aged care / community

Requirements
Must have
• Colours, fonts and logo as detailed in upload

```html
<!DOCTYPE html>
<html lang="en">
<head>
<meta charset="utf-8">
<title>Wren's Home Care – Pull-up Banner</title>
<link rel="stylesheet" href="https://fonts.googleapis.com/css2?family=Montserrat:wght@800;900&family=Poppins:wght@400;500&display=swap">
<style>
  :root {
    --crimson: #8e1230;
    --navy: #2a2636;
    --cream: #f3ebdf;
    --white: #ffffff;
    --page: #f4f4f4;
    --ink: #2b2733;
  }
  * { margin: 0; padding: 0; box-sizing: border-box; }
  html, body { width: 808px; height: 1200px; overflow: hidden; background: var(--page); }
  .banner {
    position: absolute; left: 173px; top: 40px;
    width: 462px; height: 1120px;
    background: var(--cream);
    box-shadow: 0 6px 24px rgba(0,0,0,.12);
    overflow: hidden;
    font-family: 'Poppins', sans-serif;
  }
  .masthead {
    position: absolute; left: 0; top: 0; width: 462px; height: 168px;
    background: var(--white);
    display: flex; align-items: center; justify-content: center;
  }
  .brand-name {
    color: var(--crimson); font-weight: 500;
    font-size: 36px; line-height: 1; white-space: nowrap;
  }
  .photo {
    position: absolute; left: 0; top: 168px; width: 462px; height: 360px;
    background: linear-gradient(160deg, #5f7d3c 0%, #9bb873 35%, #dfe3d4 60%, #b7c78e 85%, #4f6a31 100%);
  }
  .shapes { position: absolute; inset: 0; }
  .headline {
    position: absolute; left: 26px; top: 548px;
    font-family: 'Montserrat', sans-serif; font-weight: 900;
    text-transform: uppercase; line-height: 1;
  }
  .headline-lead { display: block; color: var(--ink); font-size: 44px; }
  .headline-main { display: block; color: var(--crimson); font-size: 60px; line-height: 60px; margin-top: 6px; letter-spacing: -.5px; }
  .divider {
    position: absolute; left: 50px; top: 722px; width: 360px; height: 1px;
    background: var(--crimson); opacity: .6;
  }
  .benefits { position: absolute; left: 36px; top: 738px; list-style: none; }
  .benefits li {
    display: flex; align-items: center; gap: 12px;
    color: var(--ink); font-size: 23px; height: 43px;
  }
  .benefits li::before {
    content: ""; width: 11px; height: 11px; border-radius: 50%;
    background: var(--crimson); flex: none;
  }
  .contact {
    position: absolute; left: 0; top: 1024px; width: 462px;
    text-align: center; color: var(--white);
  }
  .contact-phone { font-family: 'Montserrat', sans-serif; font-weight: 800; font-size: 40px; line-height: 44px; letter-spacing: 1px; }
  .contact-web { font-size: 21px; line-height: 30px; }
</style>
</head>
<body>
  <main class="banner">
    <header class="masthead">
      <span class="brand-name">Wren's Home Care</span>
    </header>

    <div class="photo" role="img" aria-label="Photo of a care worker walking outdoors with an elderly client in a leafy park"></div>

    <svg class="shapes" viewBox="0 0 462 1120" aria-hidden="true">
      <path d="M0 500 Q231 470 462 500 L462 540 L0 540 Z" fill="var(--cream)"/>
      <rect x="0" y="496" width="462" height="6" fill="var(--crimson)" transform="translate(0,0)" opacity="0"/>
      <path d="M0 498 Q231 468 462 498" fill="none" stroke="var(--crimson)" stroke-width="5"/>
      <path d="M0 1000 Q231 975 462 1000 L462 1120 L0 1120 Z" fill="var(--crimson)"/>
      <path d="M0 992 Q231 967 462 992" fill="none" stroke="var(--navy)" stroke-width="4"/>
    </svg>

    <h1 class="headline">
      <span class="headline-lead">After all its</span>
      <span class="headline-main">Your Home,<br>Your Care</span>
    </h1>

    <div class="divider"></div>

    <ul class="benefits">
      <li>Family-owned and local.</li>
      <li>Hassle-free, quality care.</li>
      <li>Peace of mind for familes</li>
      <li>Nurse-led expertise.</li>
    </ul>

    <footer class="contact">
      <div class="contact-phone">08 7394 2650</div>
      <div class="contact-web">wrenshomecare-example.com.au</div>
    </footer>
  </main>
</body>
</html>
```